Snapframe Party Rentals New Business Card*

Need a business card designed for a Photo Booth Hire company.Must look very professional and colorful.A new creative logo would be a bonus. Our current logo is attached on here.

Contact Information for Business Card

Business Name: SNAPFRAME PARTY RENTALS
Contact Person: MARCUS OKAFOR
Mobile: 0491826350
Email: INFO@SNAPFRAMERENTALS.EXAMPLE
Website: WWW.SNAPFRAMERENTALS.EXAMPLE
Facebook: WWW.FACEBOOK.COM/SNAPFRAME.PARTY.RNT

Font styles to use
Serif
Sans Serif
Script

Colors

Designer to choose colors to be used in the design.

Requirements
Must have
• Bonus if the colors match our website.

```html
<!DOCTYPE html>
<html lang="en">
<head>
<meta charset="utf-8">
<title>Snapframe Party Rentals — Business Card</title>
<link rel="stylesheet" href="https://fonts.googleapis.com/css2?family=Cinzel:wght@400&family=Oswald:wght@600&family=Mulish:wght@300;400;600&display=swap">
<style>
  :root {
    --canvas-bg: #e9e9ea;
    --card-dark: #3d3d3f;
    --card-light: #f5f5f5;
    --ink: #3a3a3c;
    --ink-soft: #6b6b6e;
    --front-type: #c4c4c6;
    --band-stripe: #8c8c8f;
  }
  * { margin: 0; padding: 0; box-sizing: border-box; }
  html, body { width: 1200px; height: 900px; overflow: hidden; }
  body {
    background: var(--canvas-bg);
    display: flex;
    flex-direction: column;
    align-items: center;
    justify-content: center;
    gap: 34px;
  }
  .card {
    width: 700px;
    height: 400px;
    position: relative;
    overflow: hidden;
    box-shadow: 0 6px 18px rgba(0,0,0,0.12);
  }

  /* Front */
  .card-front {
    background: var(--card-dark);
    display: flex;
    flex-direction: column;
    align-items: center;
    justify-content: center;
    color: var(--front-type);
  }
  .front-name {
    font-family: "Cinzel", serif;
    font-weight: 400;
    text-align: center;
    font-size: 38px;
    line-height: 1.18;
    letter-spacing: 1px;
  }
  .front-tagline {
    font-family: "Oswald", sans-serif;
    font-weight: 600;
    font-size: 11.5px;
    letter-spacing: 0.6px;
    margin-top: 8px;
  }

  /* Back */
  .card-back { background: var(--card-light); color: var(--ink); }
  .brand {
    position: absolute;
    left: 48px;
    top: 92px;
    width: 260px;
  }
  .brand-mark {
    width: 96px;
    height: 96px;
    border-radius: 50%;
    background: var(--ink);
    margin-bottom: 18px;
  }
  .brand-name {
    font-family: "Oswald", sans-serif;
    font-weight: 600;
    font-size: 30px;
    line-height: 1.02;
    letter-spacing: 0.5px;
    color: var(--ink);
  }
  .brand-web {
    font-family: "Oswald", sans-serif;
    font-weight: 600;
    font-size: 12.5px;
    letter-spacing: 0.3px;
    margin-top: 4px;
  }
  .details {
    position: absolute;
    left: 340px;
    top: 56px;
    font-family: "Mulish", sans-serif;
  }
  .person-name {
    font-size: 30px;
    font-weight: 300;
    letter-spacing: 0.5px;
    line-height: 1;
  }
  .person-name .first { font-weight: 400; }
  .person-role {
    font-size: 13px;
    font-weight: 300;
    color: var(--ink-soft);
    margin-top: 4px;
  }
  .address {
    font-size: 14.5px;
    font-weight: 300;
    line-height: 1.35;
    margin-top: 22px;
  }
  .contact-list {
    list-style: none;
    margin-top: 20px;
    font-size: 14px;
    font-weight: 300;
    line-height: 1.55;
  }
  .contact-list li { display: flex; align-items: center; gap: 8px; }
  .contact-icon { width: 11px; height: 11px; flex: none; fill: var(--ink); }
  .band { position: absolute; left: 0; bottom: 0; width: 700px; height: 400px; }
  .band-dark { fill: var(--card-dark); }
  .band-stripe { fill: var(--band-stripe); }
</style>
</head>
<body>

  <section class="card card-front">
    <h1 class="front-name">SNAPFRAME<br>PARTY RENTALS</h1>
    <p class="front-tagline">THE CITY'S MOST AFFORDABLE PARTY RENTAL COMPANY</p>
  </section>

  <section class="card card-back">
    <svg class="band" viewBox="0 0 700 400" aria-hidden="true">
      <path class="band-stripe" d="M0,384 C250,374 500,346 700,276 L700,292 C500,356 250,380 0,388 Z"/>
      <path class="band-dark" d="M0,388 C250,380 500,356 700,292 L700,400 L0,400 Z"/>
    </svg>

    <div class="brand">
      <div class="brand-mark"></div>
      <p class="brand-name">SNAPFRAME<br>PARTY RENTALS</p>
      <p class="brand-web">WWW.SNAPFRAMERENTALS.EXAMPLE</p>
    </div>

    <div class="details">
      <h2 class="person-name"><span class="first">MARCUS</span> OKAFOR</h2>
      <p class="person-role">Director</p>
      <p class="address">14th floor, Calder Lane no<br>318 Harbour Tower</p>
      <ul class="contact-list">
        <li>
          <svg class="contact-icon" viewBox="0 0 12 12" aria-hidden="true"><path d="M2.5 0.5 L4.5 0.5 L5.2 3.2 L3.8 4.3 C4.5 5.8 6.2 7.5 7.7 8.2 L8.8 6.8 L11.5 7.5 L11.5 9.5 C11.5 10.6 10.6 11.5 9.5 11.5 C4.5 11.5 0.5 7.5 0.5 2.5 C0.5 1.4 1.4 0.5 2.5 0.5 Z"/></svg>
          0491826350
        </li>
        <li>
          <svg class="contact-icon" viewBox="0 0 12 12" aria-hidden="true"><path d="M0 2 H12 V10 H0 Z M1 3 L6 6.5 L11 3 V2.8 L6 6 L1 2.8 Z" fill-rule="evenodd"/></svg>
          info@snapframerentals.example
        </li>
        <li>
          <svg class="contact-icon" viewBox="0 0 12 12" aria-hidden="true"><path d="M6 0 A6 6 0 1 0 6 12 A6 6 0 1 0 6 0 Z M6 1.2 C7 2.4 7.5 4 7.6 5.4 H4.4 C4.5 4 5 2.4 6 1.2 Z M4.4 6.6 H7.6 C7.5 8 7 9.6 6 10.8 C5 9.6 4.5 8 4.4 6.6 Z M1.3 5.4 C1.5 3.6 2.7 2.1 4.3 1.5 C3.6 2.7 3.3 4 3.2 5.4 Z M1.3 6.6 H3.2 C3.3 8 3.6 9.3 4.3 10.5 C2.7 9.9 1.5 8.4 1.3 6.6 Z M8.8 5.4 C8.7 4 8.4 2.7 7.7 1.5 C9.3 2.1 10.5 3.6 10.7 5.4 Z M8.8 6.6 H10.7 C10.5 8.4 9.3 9.9 7.7 10.5 C8.4 9.3 8.7 8 8.8 6.6 Z" fill-rule="evenodd"/></svg>
          www.snapframerentals.example
        </li>
        <li>
          <svg class="contact-icon" viewBox="0 0 12 12" aria-hidden="true"><rect x="1" y="1" width="10" height="10"/></svg>
          www.socialpage.example/snapframe.rnt
        </li>
      </ul>
    </div>
  </section>

</body>
</html>
```